New Business Card Design Project

possibly double-sided card, with one side in color. leaves, a tree branch, or a tree of life, like laurel, olive, pine ... or a seed that grows. visual discreet and stylized or naive. no photo. no human silhouette Modern Typo possibly rounded corners matte paper, no selective varnish, neither gold nor silver English brief Double sided business card, with eventually a single colored side. Leaves, a tree branch or a tree of life, laurel, olive tree, pine tree ... or a growing seed. The design has to be discreet and stylized or naive. No human silhouettes Modern made Possibly rounded corners Matte paper, no selective varnish, no gold, no silver
Updates

I really prefer toned or subtles tones, Bluish / greenwich gray, verdigris ... Elegant and discreet colors Write "HUMANISTIC HYPNOTHERAPY, SYMBOLIC THERAPY" on 2 lines and on One side only (not with the name and address) Not use pictogram (such , address...)

Contact Information for Business Card

Hypnothérapie humaniste
Thérapie symbolique

Marianne Lebrodel
Hypnothérapeute
06 48 17 20 85
47 rue des Tilleuls-Brunoy, 33710 Morvalle
cabinet.lebrodel@velmoria.fr

Colors
33b8a4
3176b5

Requirements
Must have
• sober, elegant and refined card Sober design, elegant, plain
Nice to have
• desired colors: gray, blue-gis, greyish, khaki ... Desired colors: gray, blue-gray, grayish green, khaki, ...
Should not have
• gaudy colors, bright greens no bright gold neon colors

```html
<!DOCTYPE html>
<html lang="fr">
<head>
<meta charset="utf-8">
<title>Marianne Lebrodel – Carte de visite</title>
<link rel="stylesheet" href="https://fonts.googleapis.com/css2?family=Montserrat:wght@300;400;500;700&display=swap">
<style>
  :root {
    --backdrop: #e6e8ea;
    --brand-blue: #2f79b9;
    --brand-blue-deep: #2a6ca6;
    --leaf-on-white: #d4e1ee;
    --leaf-on-white-soft: #e6eef6;
    --card-white: #ffffff;
    --text-white: #ffffff;
    --shadow: rgba(30, 40, 50, 0.18);
  }
  * { margin: 0; padding: 0; box-sizing: border-box; }
  html, body {
    width: 1200px;
    height: 1199px;
    overflow: hidden;
    background: var(--backdrop);
    font-family: "Montserrat", sans-serif;
  }
  .sheet {
    width: 1200px;
    height: 1199px;
    display: flex;
    flex-direction: column;
    align-items: center;
    justify-content: center;
    gap: 64px;
  }
  .card {
    position: relative;
    width: 760px;
    height: 492px;
    border-radius: 6px;
    overflow: hidden;
    box-shadow: 0 10px 30px var(--shadow);
  }

  /* Front: coloured side */
  .card--front { background: var(--brand-blue); }
  .card--front .foliage {
    position: absolute;
    right: 0;
    top: 0;
    width: 420px;
    height: 492px;
    background: radial-gradient(ellipse at 55% 45%, var(--brand-blue-deep) 0%, rgba(42,108,166,0.55) 45%, rgba(47,121,185,0) 75%);
  }
  .tagline {
    position: absolute;
    left: 0;
    right: 0;
    top: 206px;
    text-align: center;
    color: var(--text-white);
  }
  .tagline__main {
    font-weight: 700;
    font-size: 31px;
    letter-spacing: 0.2px;
  }
  .tagline__sub {
    margin-top: 4px;
    font-weight: 300;
    font-size: 17px;
    letter-spacing: 3.2px;
  }

  /* Back: white side */
  .card--back { background: var(--card-white); color: var(--brand-blue); }
  .card--back .foliage {
    position: absolute;
    right: 0;
    top: 0;
    width: 430px;
    height: 300px;
    background: radial-gradient(ellipse at 60% 40%, var(--leaf-on-white) 0%, var(--leaf-on-white-soft) 50%, rgba(255,255,255,0) 78%);
  }
  .identity {
    position: absolute;
    left: 52px;
    top: 196px;
  }
  .identity__name {
    font-weight: 700;
    font-size: 30px;
    line-height: 1.1;
  }
  .identity__role {
    font-weight: 400;
    font-size: 18px;
    margin-top: 2px;
  }
  .contact {
    position: absolute;
    left: 52px;
    bottom: 44px;
    list-style: none;
    font-weight: 400;
    font-size: 18px;
    line-height: 1.35;
  }
</style>
</head>
<body>
  <main class="sheet">
    <section class="card card--front">
      <div class="foliage" role="img" aria-label="Branche feuillue stylisée, ton sur ton bleu"></div>
      <div class="tagline">
        <p class="tagline__main">Hypnothérapie humaniste</p>
        <p class="tagline__sub">Thérapie symbolique</p>
      </div>
    </section>

    <section class="card card--back">
      <div class="foliage" role="img" aria-label="Branche feuillue stylisée en bleu pâle"></div>
      <div class="identity">
        <h1 class="identity__name">Marianne Lebrodel</h1>
        <p class="identity__role">Hypnothérapeute</p>
      </div>
      <ul class="contact">
        <li class="contact__phone">06 48 17 20 85</li>
        <li class="contact__email">cabinet.lebrodel@velmoria.fr</li>
        <li class="contact__address">47 rue des Tilleuls-Brunoy, 33710 Morvalle</li>
      </ul>
    </section>
  </main>
</body>
</html>
```